Karvido Nutrition Website Design. Turnkey ready to go live.

Create a small, basic website for Karvido. Mimic the design attributes and graphic elements in the sales literature and PPT presentation. White chicken, various graphics found in the literature can be used.
Keep the site simple and graphic. Here's an example: https://www.qorbel.com/website-template/view/html/4417/?siteId=7a3c19d2-5e80-4b6f-a2d1-c08e7f3b6a51&metaSiteId=b81f0e24-9d37-4c5a-a6e2-53d9e07c1f88&originUrl=https%3A%2F%2Fwww.qorbel.com%2Fwebsite%2Ftemplates%2Fhtml%2Fdesign%2Fdesigner

Also: https://www.qorbel.com/website-template/view/html/2963/?siteId=e6d2a8f0-3b41-4c97-8e15-9a7c2d04b6e3&metaSiteId=5f9b3e17-c2a8-4d06-b4f1-e8037a6c29d4&originUrl=https%3A%2F%2Fwww.qorbel.com%2Fwebsite%2Ftemplates%2Fhtml%2Fdesign%2Fdesigner

Don't get locked into the examples. They are meant as examples of the level of simplicity we're looking for. The main goal is a fast, simple site that mimics the provided literature - executted quickly.

Target Market(s)

Animal nutrition industry: production managers of livestock grow operations.

Industry/Entity Type

Nutrition

Coding

Coded - Design and coding required

Number of Pages Required

1 page

Font styles to use
Sans Serif

Requirements
Must have
• Synergy with he provided sales literature themes. Use of the provided info graphics.
• "Call us" "email us" call to action.
• 1 (800) 372-9048
• info@karvidonutrition.com (current url at brimtex)
Nice to have
• Cool scrolling that creates an interesting visual experience. Mobile version.

```html
<!DOCTYPE html>
<html lang="en">
<head>
<meta charset="utf-8">
<title>Karvido Nutrition</title>
<link href="https://fonts.googleapis.com/css2?family=Exo+2:ital,wght@0,500;0,600;1,500;1,600&family=Lato:ital,wght@0,400;0,700;1,400&display=swap" rel="stylesheet">
<style>
  :root {
    --teal: #19b8a5;
    --amber: #f3b21a;
    --lime: #8dc63f;
    --olive: #c9be1f;
    --ink: #222;
    --text: #555;
    --muted: #9a9a9a;
    --rule: #e6e6e6;
    --field: #f3f3f3;
  }
  * { box-sizing: border-box; margin: 0; padding: 0; }
  html, body { width: 830px; height: 1200px; overflow: hidden; background: #fff; }
  body { font-family: "Lato", sans-serif; color: var(--text); position: relative; }
  .abs { position: absolute; }
  .display { font-family: "Exo 2", sans-serif; font-style: italic; font-weight: 600; }

  /* header */
  .brand { left: 54px; top: 18px; display: flex; align-items: center; gap: 8px; }
  .brand-name { font-family: "Lato", sans-serif; font-weight: 700; font-size: 38px; color: var(--teal); letter-spacing: -0.5px; }
  .brand-dot { width: 10px; height: 10px; border-radius: 50%; background: var(--amber); }
  .main-nav { right: 54px; top: 24px; display: flex; gap: 26px; font-size: 12.5px; color: #b4b4b4; }
  .main-nav .active { color: var(--teal); }

  /* hero */
  .hero-photo { left: 54px; top: 152px; width: 288px; height: 288px; border-radius: 50%;
    background: radial-gradient(circle at 45% 40%, #f4efe8 0%, #d9cfc2 35%, #8a8076 70%, #5b5650 100%); }
  .hero-title { left: 394px; top: 162px; font-size: 50px; color: var(--teal); line-height: 1; }
  .hero-sub { left: 396px; top: 214px; font-family: "Lato", sans-serif; font-size: 33px; line-height: 1;
    background: linear-gradient(90deg, var(--lime), var(--olive)); -webkit-background-clip: text; background-clip: text; color: transparent; }
  .hero-copy { left: 394px; top: 264px; width: 340px; font-size: 11.5px; line-height: 1.45; }
  .newsletter-label { left: 396px; top: 330px; font-size: 21px; color: var(--ink); }
  .newsletter-form { left: 393px; top: 367px; display: flex; gap: 8px; }
  .email-field { width: 252px; height: 36px; border-radius: 18px; background: var(--field); border: 1px solid #cfcfcf;
    font-family: "Lato", sans-serif; font-style: italic; font-size: 10px; color: #bbb; padding-left: 22px; }
  .subscribe { width: 124px; height: 36px; border-radius: 18px; border: 0; font-family: "Lato", sans-serif; font-weight: 700;
    font-size: 14px; color: #1b2b2a; background: linear-gradient(90deg, var(--teal), var(--amber)); }

  .rule { left: 54px; width: 722px; height: 1px; background: var(--rule); }

  /* heat stress */
  .section-title { font-size: 36px; line-height: 1; }
  .section-title .t { color: var(--teal); }
  .section-title .a { color: var(--amber); }
  .heat-title { left: 0; width: 830px; top: 556px; text-align: center; }
  .stat { top: 610px; width: 180px; text-align: center; }
  .stat-ring { width: 116px; height: 116px; margin: 0 auto; border-radius: 50%; background: #fff;
    box-shadow: 0 0 0 3px #f4f4f4, 0 2px 10px rgba(0,0,0,0.08); position: relative; }
  .stat-value { position: absolute; top: 28px; left: 0; right: 0; font-family: "Lato", sans-serif; font-size: 40px; color: #4a4a4a; }
  .stat-value small { font-size: 10px; }
  .stat-arrow { position: absolute; left: 51px; top: 80px; }
  .stat-trend { margin-top: 22px; font-family: "Exo 2", sans-serif; font-style: italic; font-size: 12px; font-weight: 500; }
  .stat-trend.up { color: var(--teal); }
  .stat-trend.down { color: var(--amber); }
  .stat-name { margin-top: 6px; font-family: "Exo 2", sans-serif; font-style: italic; font-size: 17px; color: var(--ink); line-height: 1.1; }

  /* about / effects */
  .col-title { top: 886px; }
  .col-copy { top: 940px; font-size: 10px; line-height: 1.6; color: #666; }
  .effects-list { left: 301px; top: 984px; list-style: none; font-size: 10px; font-weight: 700; color: #555; }
  .effects-list li { margin-bottom: 10px; padding-left: 16px; position: relative; }
  .effects-list li::before { content: ""; position: absolute; left: 1px; top: 4px; width: 4px; height: 4px; border-radius: 50%; background: #555; }
  .lab-photo { left: 546px; top: 890px; width: 230px; height: 128px;
    background: linear-gradient(180deg, #e7e9ec 0%, #cfd3d8 55%, #a9aeb4 100%); }
  .slider-dots { left: 650px; top: 1005px; display: flex; gap: 4px; }
  .slider-dots span { width: 4px; height: 4px; border-radius: 50%; background: #fff; }
  .slider-dots span.on { width: 7px; height: 7px; margin-top: -1.5px; border: 1.5px solid #fff; background: #333; }

  /* footer */
  .footer-nav { left: 54px; top: 1104px; display: flex; gap: 16px; font-size: 10.5px; color: #888; }
  .footer-nav .active { color: var(--amber); }
  .footer-split { left: 414px; top: 1094px; width: 1px; height: 30px; background: #d8d8d8; }
  .contact { left: 446px; top: 1091px; display: flex; align-items: center; gap: 8px; }
  .contact-label { font-size: 10px; font-style: italic; color: var(--muted); }
  .contact-phone { font-size: 21px; color: #555; line-height: 1; }
  .copyright { left: 0; width: 830px; top: 1168px; text-align: center; font-size: 10px; color: #999; }
  .copyright .name { font-family: "Lato", sans-serif; font-size: 14px; color: var(--teal); }
</style>
</head>
<body>

<header>
  <div class="abs brand"><span class="brand-name">Karvido</span><span class="brand-dot"></span></div>
  <nav class="abs main-nav">
    <span class="active">Home</span><span>About Us</span><span>Heat Stress</span><span>Effects</span><span>US Headquarters</span><span>Contact Us</span>
  </nav>
</header>

<section class="hero">
  <div class="abs hero-photo" role="img" aria-label="White broiler chicken walking, cropped in a circle"></div>
  <h1 class="abs hero-title display">Animal Nutrition</h1>
  <p class="abs hero-sub">Health &amp; Ends with the gut.</p>
  <p class="abs hero-copy">Lorem Ipsum is simply dummy text of the printing and typesetting industry. Lorem Ipsum has been the industry's</p>
  <p class="abs newsletter-label display">newsletter</p>
  <form class="abs newsletter-form">
    <input class="email-field" type="text" placeholder="E-Mail Address">
    <button class="subscribe" type="button">SUBSCRIBE</button>
  </form>
</section>

<div class="abs rule" style="top:514px"></div>

<section class="heat">
  <h2 class="abs heat-title section-title display"><span class="t">Heat</span> <span class="a">Stress</span></h2>

  <div class="abs stat" style="left:51px">
    <div class="stat-ring"><div class="stat-value">3<small>%</small></div>
      <svg class="stat-arrow" width="14" height="8"><polygon points="0,8 7,0 14,8" fill="#f3b21a"/></svg></div>
    <p class="stat-trend up">INCREASED</p><p class="stat-name">Weight gain</p>
  </div>
  <div class="abs stat" style="left:234px">
    <div class="stat-ring"><div class="stat-value">5.8<small>%</small></div>
      <svg class="stat-arrow" width="14" height="8"><polygon points="0,0 14,0 7,8" fill="#19b8a5"/></svg></div>
    <p class="stat-trend down">DECREASED</p><p class="stat-name">Feed conversion<br>ratio</p>
  </div>
  <div class="abs stat" style="left:417px">
    <div class="stat-ring"><div class="stat-value">55<small>%</small></div>
      <svg class="stat-arrow" width="14" height="8"><polygon points="0,0 14,0 7,8" fill="#19b8a5"/></svg></div>
    <p class="stat-trend down">DECREASED</p><p class="stat-name">Lesion scores</p>
  </div>
  <div class="abs stat" style="left:600px">
    <div class="stat-ring"><div class="stat-value">48<small>%</small></div>
      <svg class="stat-arrow" width="14" height="8"><polygon points="0,0 14,0 7,8" fill="#19b8a5"/></svg></div>
    <p class="stat-trend down">DECREASED</p><p class="stat-name">Family Law</p>
  </div>
</section>

<div class="abs rule" style="top:839px"></div>

<section class="about">
  <h2 class="abs col-title section-title display" style="left:54px"><span class="t">About</span> <span class="a">Us</span></h2>
  <p class="abs col-copy" style="left:55px;width:200px">Lorem Ipsum is simply dummy text of the printing and typesetting industry. Lorem Ipsum has been the industry's standard dummy text ever since the 1500s, when an unknown printer took a galley.</p>
</section>

<section class="effects">
  <h2 class="abs col-title section-title display" style="left:301px"><span class="t">Effects</span></h2>
  <p class="abs col-copy" style="left:301px;width:230px">Lorem Ipsum is simply dummy text of the printing and typesetting industry.</p>
  <ul class="abs effects-list"><li>Body Weight Gain(Kg)</li><li>Feed Conversion Ratio(Kg)</li></ul>
</section>

<div class="abs lab-photo" role="img" aria-label="Research laboratory interior with benches and equipment"></div>
<div class="abs slider-dots"><span class="on"></span><span></span><span></span><span></span></div>

<div class="abs rule" style="top:1070px"></div>

<footer>
  <nav class="abs footer-nav">
    <span class="active">Home</span><span>About</span><span>Heat stress</span><span>Effects</span><span>US Headquarters</span><span>Contact</span>
  </nav>
  <div class="abs footer-split"></div>
  <div class="abs contact">
    <svg width="40" height="40" viewBox="0 0 40 40">
      <circle cx="20" cy="20" r="19" fill="none" stroke="#19b8a5" stroke-width="1.2" stroke-dasharray="1.5 2.5"/>
      <path d="M15 13c-1 1-1.5 2.5-.5 4.5 1.5 3 4 5.5 7 7 2 1 3.5.5 4.5-.5l-2.5-2.5-2 1c-1.5-.8-3-2.3-3.8-3.8l1-2z" fill="none" stroke="#f3b21a" stroke-width="1.2" stroke-linejoin="round"/>
    </svg>
    <div><p class="contact-label">Contact us now</p><p class="contact-phone">1 (800) 372-9048</p></div>
  </div>
  <div class="abs rule" style="top:1153px"></div>
  <p class="abs copyright">© <span class="name">Karvido Nutrition</span> - 2017. All Rights Reserved</p>
</footer>

</body>
</html>
```